Veltorix needs web site design

We need a web site design for our product called 'Veltorix'. We develop an asset management system that can manage all kind of assets. Currently we have a logo theme and would like to use similar color scheme; the content concept is pretty much in http://tbaldwyn.example but the product was called "Keystone Lab" at the time and is now called "Veltorix". Velto means Unified Ledger Tracking Operations Network Agency.
Please use generic image for asset (not just bridges) e.g buildings, trucks, powerlines. train, bus, lightrail etc..
Please emphazise on the data management and security, and distributed networking.

the new website address is https://www.veltorix.example/

name on business card

Thomas Baldwyn 555-014-7723
Principal Architect / Software Engineer

Dana Baldwyn 555-018-2946
Software Engineer

Coding

Coded - Design and coding required

Number of Pages Required

1 page

```html
<!DOCTYPE html>
<html lang="en">
<head>
<meta charset="utf-8">
<title>Veltorix</title>
<link href="https://fonts.googleapis.com/css2?family=Mukta:wght@400;500;600;700&family=Open+Sans:wght@400;600;700&display=swap" rel="stylesheet">
<style>
:root{
  --navy:#15237d;
  --gold:#c9a24a;
  --gold-light:#f3c865;
  --ink:#2b2b2b;
  --panel:#e2e5ee;
  --white:#ffffff;
}
*{box-sizing:border-box;margin:0;padding:0}
html,body{width:934px;height:1200px;overflow:hidden;background:var(--white)}
body{position:relative;font-family:"Open Sans",sans-serif;color:var(--ink)}
.brand{position:absolute;display:flex;align-items:center;gap:8px;font-family:"Mukta",sans-serif;font-weight:700;font-size:32px;line-height:1;letter-spacing:-.5px}
.brand-mark{width:26px;height:26px;border:3px solid currentColor}
.site-header .brand{left:94px;top:16px;color:var(--navy)}
.main-nav{position:absolute;top:35px;left:0;width:934px;height:18px}
.main-nav a{position:absolute;font-size:11px;color:var(--gold);text-decoration:none}
.main-nav a.current{color:var(--navy)}
.hero{position:absolute;left:94px;top:84px;width:746px;height:323px;overflow:hidden}
.hero-bg{position:absolute;inset:0;background:linear-gradient(120deg,#3a4a7a 0%,#2c3d6d 45%,#1f3266 75%,#27386a 100%)}
.hero-bg::after{content:"";position:absolute;left:0;right:0;bottom:0;height:90px;background:linear-gradient(180deg,rgba(0,0,0,0),rgba(120,90,90,.35))}
.hero-title{position:absolute;left:42px;top:44px;font-family:"Mukta",sans-serif;font-weight:400;font-size:38px;color:var(--white);letter-spacing:.5px;line-height:1}
.hero-list{position:absolute;left:42px;top:100px;list-style:none;font-family:"Mukta",sans-serif;font-size:21px;line-height:30px;color:var(--gold-light)}
.hero-list b{font-weight:700}
.hero-list span{font-weight:400}
.btn{position:absolute;left:42px;top:242px;width:97px;height:34px;background:var(--gold);color:var(--white);font-size:10px;font-weight:700;display:flex;align-items:center;justify-content:center;letter-spacing:.3px}
.dots{position:absolute;top:295px;left:340px;display:flex;gap:8px}
.dots i{width:11px;height:11px;border:2px solid #d8dce8;border-radius:50%}
.dots i.on{background:#4a8fe0}
.pitch{position:absolute;left:94px;top:461px;width:746px;height:263px;background:var(--panel);border-radius:14px;overflow:hidden}
.pitch h2{position:absolute;left:27px;top:78px;font-family:"Mukta",sans-serif;font-weight:400;font-size:24px;line-height:40px;color:var(--navy);letter-spacing:.2px}
.pitch-art{position:absolute;left:444px;top:27px;width:270px;height:220px;border-radius:8px;background:linear-gradient(180deg,#5b5fd6 0%,#8d8ee0 60%,#dfe1ee 100%)}
.features{position:absolute;top:782px;left:0;width:934px}
.feature{position:absolute;top:0}
.feature-icon{width:66px;height:64px;border-radius:8px;background:linear-gradient(180deg,#fafafa,#e6e6e6);box-shadow:0 3px 6px rgba(0,0,0,.18);display:flex;align-items:center;justify-content:center}
.feature h3{margin-top:20px;font-family:"Mukta",sans-serif;font-weight:600;font-size:19px;color:var(--gold);line-height:1.2}
.feature p{margin-top:16px;font-size:10.5px;line-height:15px;color:var(--ink)}
.site-footer{position:absolute;left:94px;top:1058px;width:746px;height:115px;background:var(--gold)}
.site-footer .brand{left:20px;top:20px;color:var(--white)}
.social{position:absolute;top:13px;display:flex;gap:5px;left:675px}
.social i{width:23px;height:23px;border:1.5px solid var(--white);border-radius:50%}
.foot-nav a{position:absolute;top:82px;font-size:11px;color:var(--white);text-decoration:none}
.copyright{position:absolute;right:18px;top:83px;font-size:9px;color:var(--white)}
</style>
</head>
<body>
<header class="site-header">
  <div class="brand"><span class="brand-mark"></span>Veltorix</div>
  <nav class="main-nav">
    <a class="current" href="#" style="left:539px">Home</a>
    <a href="#" style="left:598px">Portfolio</a>
    <a href="#" style="left:669px">Download</a>
    <a href="#" style="left:746px">About</a>
    <a href="#" style="left:805px">Contact</a>
  </nav>
</header>

<section class="hero">
  <div class="hero-bg" role="img" aria-label="Photo of high-voltage power line towers against a blue evening sky"></div>
  <h1 class="hero-title">SERVICE</h1>
  <ul class="hero-list">
    <li><b>Sotware development</b></li>
    <li><b>Web &amp; Network</b></li>
    <li><b>Software</b> <span>project</span></li>
    <li><b>Computing</b> <span>consultant</span></li>
  </ul>
  <a class="btn">SEE MORE</a>
  <div class="dots"><i class="on"></i><i></i><i></i><i></i></div>
</section>

<section class="pitch">
  <h2>COMPUTING SUPPORT OF<br>COMPLEX DATABASES, NETWORKS,<br>WORKSTATIONS AND SERVERS.</h2>
  <div class="pitch-art" role="img" aria-label="Illustration of three developers with laptops sitting in front of a large screen showing code"></div>
</section>

<section class="features">
  <article class="feature" style="left:94px;width:208px">
    <div class="feature-icon">
      <svg width="40" height="40" viewBox="0 0 40 40" fill="none" stroke="#1c2450" stroke-width="1.6">
        <rect x="9" y="16" width="22" height="15" rx="1"/><path d="M20 31v4M14 36h12"/>
        <rect x="15" y="21" width="10" height="7"/><path d="M17 21v-2a3 3 0 0 1 6 0v2"/>
        <rect x="2" y="5" width="8" height="6"/><rect x="30" y="5" width="8" height="6"/>
        <path d="M10 8h20M20 8v8"/><circle cx="20" cy="8" r="1.5"/>
      </svg>
    </div>
    <h3>Data management</h3>
    <p>It is a long established fact that a reader will be distracted by the readable content of a page when looking at its layout. The point of using Lorem Ipsum is that it has a more-or-less normal distribution of letters, as opposed to using 'Content here, content here', making it look like readable English.</p>
  </article>
  <article class="feature" style="left:356px;width:216px">
    <div class="feature-icon">
      <svg width="40" height="40" viewBox="0 0 40 40" fill="none" stroke="#1c2450" stroke-width="1.8">
        <path d="M20 3l14 5v10c0 9-6 15-14 19C12 33 6 27 6 18V8z"/>
        <path d="M20 8l9 3v7c0 6-4 10-9 13-5-3-9-7-9-13v-7z"/>
        <circle cx="20" cy="19" r="5"/><path d="M17.5 19l2 2 3-3.5"/>
      </svg>
    </div>
    <h3>Security</h3>
    <p>Many desktop publishing packages and web page editors now use Lorem Ipsum as their default model text, and a search for 'lorem ipsum' will uncover many web sites still in their infancy. Various versions have evolved over the years, sometimes by accident, some-times on purpose (injected humour and the</p>
  </article>
  <article class="feature" style="left:626px;width:222px">
    <div class="feature-icon">
      <svg width="40" height="40" viewBox="0 0 40 40" fill="none" stroke="#1c2450" stroke-width="1.6">
        <path d="M10 18a6 6 0 0 1 2-11 8 8 0 0 1 15 1 5 5 0 0 1 3 10z"/>
        <path d="M20 18v5M8 23h24M8 23v4M20 23v4M32 23v4"/>
        <rect x="3" y="27" width="10" height="4"/><rect x="3" y="32" width="10" height="4"/>
        <rect x="15" y="27" width="10" height="4"/><rect x="15" y="32" width="10" height="4"/>
        <rect x="27" y="27" width="10" height="4"/><rect x="27" y="32" width="10" height="4"/>
      </svg>
    </div>
    <h3>Distributed networking</h3>
    <p>Lorem ipsum' will uncover many web sites still in their infancy. Various versions have evolved over the years, sometimes by accident, some-times on purpose (injected humour and the like).<br>It is a long established fact that a reader will be distracted by the readable content of a page</p>
  </article>
</section>

<footer class="site-footer">
  <div class="brand"><span class="brand-mark"></span>Veltorix</div>
  <div class="social"><i aria-label="Professional network"></i><i aria-label="Social network"></i></div>
  <nav class="foot-nav">
    <a href="#" style="left:19px">Home</a>
    <a href="#" style="left:80px">Portfolio</a>
    <a href="#" style="left:154px">Download</a>
    <a href="#" style="left:235px">About</a>
    <a href="#" style="left:296px">Contact</a>
  </nav>
  <p class="copyright">Copyright © Harlow &amp; Associates 2009</p>
</footer>
</body>
</html>
```